Estate Planning Law Firm opening new branch in Florida

I am an experienced estate planning attorney that recently relocated to Florida. Looking for a banner Ad to place on platforms such as YardLoop, Chatterly and Pixmora to create publicity for firm and new leads.

```html
<!DOCTYPE html>
<html lang="en">
<head>
<meta charset="UTF-8">
<title>Calmora Law Firm – Florida Estate Planning</title>
<link href="https://fonts.googleapis.com/css2?family=Poppins:wght@500;600;700&display=swap" rel="stylesheet">
<style>
  :root {
    --green: #0e6b3b;
    --green-bright: #3db54a;
    --green-lime: #7cc242;
    --navy: #1d3045;
    --ink: #111111;
    --paper: #f4f5f6;
    --mist: #d9dcdf;
    --white: #ffffff;
  }
  * { margin: 0; padding: 0; box-sizing: border-box; }
  html, body { width: 1200px; height: 702px; overflow: hidden; background: var(--white); }
  .banner {
    position: relative;
    width: 1200px;
    height: 702px;
    overflow: hidden;
    background: var(--paper);
    font-family: "Poppins", sans-serif;
  }
  .skyline {
    position: absolute;
    left: 0; bottom: 0;
    width: 820px; height: 420px;
    background: linear-gradient(180deg, rgba(244,245,246,0) 0%, #c9ccd0 55%, #9fa4aa 100%);
    opacity: .8;
  }
  .dot-field {
    position: absolute;
    right: 0; top: 0;
    width: 420px; height: 240px;
    background: radial-gradient(ellipse at top right, #cfd2d5 0%, rgba(244,245,246,0) 70%);
  }
  .brand-band {
    position: absolute;
    left: 0; top: 126px;
    width: 416px; height: 68px;
    background: var(--white);
    display: flex;
    align-items: center;
    padding-left: 115px;
    gap: 12px;
  }
  .brand-mark { width: 30px; height: 30px; background: var(--green); }
  .brand-name {
    font-weight: 600;
    font-size: 19px;
    line-height: 1.1;
    color: var(--navy);
    letter-spacing: .5px;
  }
  .headline {
    position: absolute;
    left: 109px; top: 240px;
    font-weight: 700;
    font-size: 44px;
    line-height: 55px;
    color: var(--green);
  }
  .services {
    position: absolute;
    left: 109px; top: 420px;
    font-weight: 700;
    font-size: 17px;
    line-height: 25px;
    color: var(--ink);
  }
  .pill {
    position: absolute;
    display: flex;
    align-items: center;
    justify-content: center;
    border-radius: 12px;
    color: var(--white);
  }
  .call-now {
    left: 109px; top: 524px;
    width: 168px; height: 47px;
    background: var(--green);
    font-weight: 600;
    font-size: 23px;
  }
  .phone {
    left: 109px; top: 577px;
    width: 220px; height: 50px;
    background: var(--ink);
    font-weight: 500;
    font-size: 16px;
    border-radius: 14px;
  }
  .social { position: absolute; left: 376px; display: flex; align-items: center; }
  .social-chatterly { top: 527px; }
  .social-pixmora { top: 595px; }
  .social-dot {
    width: 32px; height: 32px;
    border-radius: 50%;
    background: var(--ink);
    position: relative;
    z-index: 1;
  }
  .social-handle {
    margin-left: -10px;
    width: 200px; height: 32px;
    background: var(--green);
    border-radius: 8px;
    color: var(--white);
    font-weight: 500;
    font-size: 20px;
    display: flex;
    align-items: center;
    padding-left: 40px;
  }
  .rings { position: absolute; left: 0; top: 0; }
  .portrait {
    position: absolute;
    left: 705px; top: 120px;
    width: 430px; height: 582px;
    border-radius: 215px 215px 0 0;
    background: linear-gradient(180deg, #3a2a22 0%, #263246 30%, #1f2a3d 100%);
  }
</style>
</head>
<body>
  <main class="banner">
    <div class="skyline" role="img" aria-label="Faded photo of a Florida city skyline by the water"></div>
    <div class="dot-field" role="img" aria-label="Soft grey dotted wave texture"></div>

    <svg class="rings" width="1200" height="702" viewBox="0 0 1200 702" aria-hidden="true">
      <g fill="none">
        <circle cx="918" cy="459" r="262" stroke="var(--mist)" stroke-width="26"/>
        <path d="M 680 350 A 262 262 0 0 1 780 236" stroke="var(--green-lime)" stroke-width="26"/>
        <path d="M 1160 380 A 262 262 0 0 1 1110 640" stroke="var(--green-bright)" stroke-width="26"/>
        <circle cx="918" cy="459" r="225" stroke="var(--navy)" stroke-width="20"/>
        <path d="M 700 520 A 225 225 0 0 1 720 360" stroke="var(--green-lime)" stroke-width="20"/>
        <path d="M 1143 470 A 225 225 0 0 1 1100 600" stroke="var(--green-bright)" stroke-width="20"/>
        <circle cx="918" cy="459" r="196" stroke="var(--mist)" stroke-width="12"/>
      </g>
    </svg>
    <div class="portrait" role="img" aria-label="Photo of a smiling attorney in a navy suit and blue tie with arms crossed"></div>

    <div class="brand-band">
      <span class="brand-mark"></span>
      <span class="brand-name">CALMORA<br>LAW FIRM, PLLC</span>
    </div>

    <h1 class="headline">Florida Estate Planning:<br>Secure Your Legacy<br>Today!</h1>
    <p class="services">Wills, Trusts, Powers of Attorney &amp; More.<br>Free Consultation!</p>

    <div class="pill call-now">Call Now</div>
    <div class="pill phone">+305 555 0147 2468</div>

    <div class="social social-chatterly">
      <span class="social-dot"></span>
      <span class="social-handle">Calmora</span>
    </div>
    <div class="social social-pixmora">
      <span class="social-dot"></span>
      <span class="social-handle">Calmora</span>
    </div>
  </main>
</body>
</html>
```